Luxury Jewelry & Watch Company Website Design

At Vexaro, we are a brand that designs and sells unique Jewelry & Watches for Men and Women. We are looking to transform our current e-commerce website, which looks like a boring catalog, into a more EXCLUSIVE, luxurious, and unique website experience... CLASSY, yet MODERN...We want customers/ clients to be drawn into our brand and our products.. essentially to turn them into buying customers. We want them to feel the exclusiveness of our brand and how different we are from the rest of the industry. The website has to convey the feel and culture of our brand, but stay simple to navigate.

We sell direct to the consumer online as well as wholesale to retailers, And now we are opening our first store in March..So the website should appeal to all areas. Id like to have a place on the website for our upcoming store, it would be sweet to have an area where clients can setup an appointment to meet with me at the store to go over and Jewelry, watches, or Custom Jewelry Design. In March, we will have professional photos of the store as well as professional photos of models wearing the Jewelry & Watches. So please make space for all of those new photos to be implemented.

That should be it! It all comes down to creating a Luxurious, Exclusive, and Unique website that portrays Vexaro and brings in clientele and seals the deal for sales!

Thank you very much! We are extremely excited to see all your awesome designs!

Target Market(s)

25-40 year old successful Men & Women... The young professionals crowd.

Industry/Entity Type

E-Commerce

Requirements
Must have
• Luxury, Exclusive feeling (like Corvane, Marrow Peak Vodka, ext), Simplicity, Brand Culture, Watches are our main product, Appeal to both Men & Women. Also, an elegant banner for promotions, that i am able to update myself.
Nice to have
• Store Appointment Scheduler, updated area that shows which celebs/ stars are wearing the goods, History of the brand and products

```html
<!DOCTYPE html>
<html lang="en">
<head>
<meta charset="utf-8">
<title>Vexaro — Jewelry &amp; Watches</title>
<link href="https://fonts.googleapis.com/css2?family=Noto+Serif:wght@400&family=Arimo:wght@400;700&display=swap" rel="stylesheet">
<style>
:root{
  --page:#0d0d0d;
  --panel:#0f0f0f;
  --panel-edge:#2a2a2a;
  --header-top:#ffffff;
  --header-bottom:#c9c9c9;
  --ink:#111;
  --title:#f2f2f2;
  --body:#8a8a8a;
  --link:#a9a9a9;
  --cell:#3a3a3a;
  --cell-text:#e6e6e6;
  --today:#6fa6bd;
  --footer:#070707;
  --footer-text:#3e3e3e;
  --serif:'Noto Serif', Georgia, serif;
  --sans:'Arimo', Arial, sans-serif;
}
*{margin:0;padding:0;box-sizing:border-box}
html,body{width:1200px;height:1172px;overflow:hidden}
body{position:relative;background:radial-gradient(ellipse at 50% 30%,#1c1c1c 0%,#0e0e0e 55%,#090909 100%);font-family:var(--sans)}
.abs{position:absolute}

.site-header{left:0;top:0;width:1200px;height:93px;background:linear-gradient(var(--header-top),var(--header-bottom));border-bottom:1px solid #8d8d8d}
.brand{left:180px;top:24px;font:400 44px/1 var(--serif);color:var(--ink);letter-spacing:1px}
.search{left:875px;top:14px;width:140px;height:25px;background:#fff;border:1px solid #8f8f8f;font:11px/23px var(--sans);color:#888;padding-left:6px}
.search svg{position:absolute;right:6px;top:6px}
.main-nav{right:184px;top:56px;display:flex;gap:0;font:400 12px/16px var(--serif);color:var(--ink)}
.main-nav span.sep{margin:0 10px;font-size:6px;line-height:16px}

.banner{left:200px;top:150px;width:800px;height:330px;border:2px solid #3d4448;background:radial-gradient(ellipse at 50% 5%,#b4c9d1 0%,#7e949c 35%,#46555c 75%,#394348 100%);box-shadow:0 10px 30px #000}
.arrow{width:32px;height:32px;border-radius:50%;background:#1b1b1b;box-shadow:0 2px 6px #000;color:#ccc;font:12px/32px var(--sans);text-align:center}

.card{top:503px;width:257px;height:258px;border:2px solid #1f1f1f;background:var(--panel);text-align:center}
.card h2{font:400 14.5px/1 var(--serif);color:var(--title);margin-top:17px;letter-spacing:.3px}
.history p{font:10.5px/20.3px var(--sans);color:var(--body);margin:15px 14px 0}
.more{position:absolute;left:0;right:0;font:10.5px var(--sans);color:var(--link);text-decoration:underline}

.calendar{left:31px;top:40px;width:193px;height:186px;background:linear-gradient(#d9d9d9,#bdbdbd);border-radius:3px}
.calendar .month{height:26px;background:linear-gradient(#3a3535,#241f1f);border-radius:3px 3px 0 0;color:#eee;font:700 10px/26px var(--sans);position:relative}
.calendar .month i{position:absolute;top:0;font-style:normal;font-size:8px;color:#bbb}
.calendar .wk{display:grid;grid-template-columns:repeat(7,25.4px);padding-left:8px;margin-top:10px;font:700 8px var(--sans);color:#666}
.calendar .days{display:grid;grid-template-columns:repeat(7,21px);column-gap:4.4px;row-gap:5px;padding-left:9px;margin-top:6px}
.calendar .days b{height:21px;background:var(--cell);border-radius:2px;color:var(--cell-text);font:700 9.5px/21px var(--sans)}
.calendar .days b.today{background:var(--today);color:#173542}
.calendar .days b.dim{background:#2a2a2a;color:#333}

.celebs{left:742px;border-color:#2b2b2b;padding:0}
.celebs .photo{position:absolute;inset:0;background:linear-gradient(135deg,#dadada 0%,#a8a8a8 45%,#505050 80%,#2c2c2c 100%)}
.celebs .caption{position:absolute;left:0;right:0;bottom:14px;font:400 14.5px var(--serif);color:#fff;text-shadow:0 0 3px #000,1px 1px 1px #000}

.products{left:200px;top:805px;width:798px;height:258px;border:2px solid #1f1f1f;background:var(--panel)}
.products h2{position:absolute;left:27px;top:21px;font:400 14.5px var(--serif);color:var(--title)}
.products .rule{position:absolute;left:12px;right:12px;top:44px;height:1px;background:#222}
.item{position:absolute;top:66px;width:134px;text-align:center}
.item .shot{width:134px;height:117px;background:radial-gradient(circle,#e2e2e2 0%,#fff 70%)}
.item .shot.gold{background:radial-gradient(circle,#e0c26a 0%,#f6ecd0 45%,#fff 75%)}
.item .shot.dark{background:radial-gradient(circle,#6a6a6a 0%,#d8d8d8 45%,#fff 75%)}
.item p{font:10.5px/15px var(--sans);color:var(--body);margin-top:17px}

.site-footer{left:0;top:1099px;width:1200px;height:73px;background:var(--footer)}
.footer-links{left:193px;top:18px;font:10px var(--sans);color:var(--footer-text)}
.copyright{left:193px;top:42px;font:10px var(--sans);color:var(--footer-text)}
.social{left:858px;top:25px;display:flex;gap:11px}
.social span{width:24px;height:24px;border-radius:3px;background:#262626}
</style>
</head>
<body>

<header class="site-header abs">
  <div class="brand abs">Vexaro</div>
  <div class="search abs">Search
    <svg width="10" height="10" viewBox="0 0 10 10"><circle cx="4" cy="4" r="3" fill="none" stroke="#aaa" stroke-width="1.4"/><line x1="6.2" y1="6.2" x2="9" y2="9" stroke="#aaa" stroke-width="1.4"/></svg>
  </div>
  <nav class="main-nav abs">
    <span>Home</span><span class="sep">◆</span>
    <span>About Us</span><span class="sep">◆</span>
    <span>Products</span><span class="sep">◆</span>
    <span>Store Appointment</span><span class="sep">◆</span>
    <span>Contact Us</span>
  </nav>
</header>

<section class="banner abs" role="img" aria-label="Promotional banner: six silver and diamond rings standing in a row with reflections"></section>
<div class="arrow abs" style="left:181px;top:300px">‹</div>
<div class="arrow abs" style="left:985px;top:300px">›</div>

<section class="card history abs" style="left:200px">
  <h2>HISTORY OF THE COMPANY</h2>
  <p>Sed imperdiet vestibulum neque eu convallis. Sed tincidunt libero at lorem rhoncus eu hendrerit diam placerat. Integer convallis nisl at urna ullam-corper vitae feugiat nulla dignissim. Class aptent taciti sociosqu ad litora torquent per conubia nostra, per inceptos himenaeos. Suspendisse vitae placerat lacus. Duis sed metus vel urna viverra pretium sed at ipsum.</p>
  <span class="more" style="top:234px">Read more....</span>
</section>

<section class="card appointment abs" style="left:471px">
  <h2>STORE APPOINTMENT</h2>
  <div class="calendar abs">
    <div class="month"><i style="left:9px">◀</i>OCTOBER<i style="right:9px">▶</i></div>
    <div class="wk"><span>MON</span><span>TUE</span><span>WED</span><span>THU</span><span>FRI</span><span>SAT</span><span>SUN</span></div>
    <div class="days">
      <b>1</b><b>2</b><b>3</b><b>4</b><b>5</b><b>6</b><b>7</b>
      <b>8</b><b>9</b><b>10</b><b>11</b><b>12</b><b>13</b><b>14</b>
      <b>15</b><b>16</b><b>17</b><b>18</b><b>19</b><b>20</b><b>21</b>
      <b>22</b><b>23</b><b class="today">24</b><b>25</b><b>26</b><b>27</b><b>28</b>
      <b>29</b><b>30</b><b>31</b><b class="dim">1</b><b class="dim">2</b><b class="dim">3</b><b class="dim">4</b>
    </div>
  </div>
  <span class="more" style="top:241px">View more....</span>
</section>

<section class="card celebs abs">
  <div class="photo" role="img" aria-label="Black and white photo of a well-dressed man stepping out of a luxury car"></div>
  <div class="caption">CELEBS WEARING OUR WATCHES</div>
</section>

<section class="products abs">
  <h2>OUR PRODUCTS</h2>
  <div class="rule"></div>
  <div class="item" style="left:68px"><div class="shot" role="img" aria-label="Diamond engagement ring set"></div><p>vitae tincidunt urna turpis sit amet lacus.</p></div>
  <div class="item" style="left:242px"><div class="shot" role="img" aria-label="Stack of diamond rings"></div><p>Ut ornare libero ut lacus malesuada vel</p></div>
  <div class="item" style="left:416px"><div class="shot gold" role="img" aria-label="Gold and engraved silver band"></div><p>Duis sed metus vel urna viverra pretium</p></div>
  <div class="item" style="left:590px"><div class="shot dark" role="img" aria-label="Ring with black and white stones"></div><p>Sed tincidunt libero at lorem rhoncus eu hendrerit diam</p></div>
  <div class="arrow abs" style="left:22px;top:111px">‹</div>
  <div class="arrow abs" style="left:740px;top:111px">›</div>
</section>

<footer class="site-footer abs">
  <div class="footer-links abs">Home | About Us | Products | Store Appointment | Contact Us</div>
  <div class="copyright abs">Copyright © 2013, Vexaro, All Rights Reserved</div>
  <div class="social abs"><span></span><span></span><span></span><span></span></div>
</footer>

</body>
</html>
```